Business Card Design Project

We currently have existing logo. Looking to have nice colorful business cards done.
We would like the name of business, phone, address, email and website

Target Market(s)

25-50

Industry/Entity Type

Business

Requirements
Must have
• We are currently using
Samrakan font for our business name
Rage italic font for tag line..
you may visit our website at www.velmorista.com to get good feel

velmorista means colors in India. google velmorista to get more info

```html
<!DOCTYPE html>
<html lang="en">
<head>
<meta charset="utf-8">
<title>Velmorista – Business Card</title>
<link href="https://fonts.googleapis.com/css2?family=Arimo:wght@400;700&display=swap" rel="stylesheet">
<style>
  :root {
    --page-bg: #ffffff;
    --label-ink: #222222;
    --maroon-deep: #2e0606;
    --maroon: #5c0b0b;
    --crimson: #9a1414;
    --ornament-red: #c23a3a;
    --ornament-soft: #e8a3a3;
    --card-white: #ffffff;
    --ink: #1a1a1a;
  }
  * { box-sizing: border-box; margin: 0; padding: 0; }
  html, body {
    width: 1200px; height: 370px; overflow: hidden;
    background: var(--page-bg);
    font-family: "Arimo", Arial, sans-serif;
  }
  .sheet { position: relative; width: 1200px; height: 370px; }
  .card-label {
    position: absolute; top: 4px;
    font-size: 15px; color: var(--label-ink);
  }
  .card-label--back { left: 0; }
  .card-label--front { left: 634px; }
  .card {
    position: absolute; top: 28px;
    width: 566px; height: 330px; overflow: hidden;
  }
  .card--back {
    left: 0;
    background: linear-gradient(90deg, var(--maroon-deep) 0%, var(--maroon) 45%, var(--crimson) 100%);
  }
  .card--front { left: 634px; background: var(--card-white); }

  .ornament { position: absolute; border-radius: 50%; }
  .card--back .ornament {
    width: 430px; height: 430px; left: 230px; top: -50px;
    background: radial-gradient(circle, transparent 0 30%, rgba(194,58,58,0.55) 45%, rgba(194,58,58,0.25) 62%, transparent 72%);
  }
  .card--front .ornament {
    width: 460px; height: 460px; left: 215px; top: -40px;
    background: radial-gradient(circle, transparent 0 30%, var(--ornament-red) 42%, var(--ornament-soft) 58%, transparent 70%);
  }

  .brand { position: absolute; color: var(--card-white); }
  .brand__name { font-weight: 400; letter-spacing: 1px; line-height: 1; }
  .brand__tagline { font-weight: 400; line-height: 1; }

  .card--back .brand { left: 100px; top: 128px; }
  .card--back .brand__name { font-size: 66px; }
  .card--back .brand__tagline { font-size: 17px; margin: 10px 0 0 240px; }

  .front-band {
    position: absolute; left: 0; top: 0; width: 100%; height: 94px;
    background: linear-gradient(90deg, var(--maroon-deep) 0%, var(--maroon) 50%, var(--crimson) 100%);
  }
  .card--front .brand { left: 10px; top: 16px; }
  .card--front .brand__name { font-size: 38px; }
  .card--front .brand__tagline { font-size: 11px; margin: 6px 0 0 90px; }

  .contact {
    position: absolute; left: 14px; top: 116px;
    font-size: 21px; line-height: 28px; color: var(--ink);
    list-style: none;
  }
  .website {
    position: absolute; left: 14px; top: 285px;
    font-size: 21px; line-height: 28px; color: var(--ink);
  }
</style>
</head>
<body>
<main class="sheet">
  <p class="card-label card-label--back">Business Card Back</p>
  <p class="card-label card-label--front">Business Card Front</p>

  <section class="card card--back">
    <div class="ornament" role="img" aria-label="Red circular mandala ornament"></div>
    <div class="brand">
      <p class="brand__name">velmorista</p>
      <p class="brand__tagline">India Restaurant</p>
    </div>
  </section>

  <section class="card card--front">
    <div class="ornament" role="img" aria-label="Red circular mandala ornament"></div>
    <div class="front-band">
      <div class="brand">
        <p class="brand__name">velmorista</p>
        <p class="brand__tagline">India Restaurant</p>
      </div>
    </div>
    <ul class="contact">
      <li>2718 Marlow Avenue</li>
      <li>Fairbrook, CA 95210</li>
      <li>P 408.555.0142</li>
      <li>F 408.555.0143</li>
      <li>E info@velmorista.com</li>
    </ul>
    <p class="website">www.velmorista.com</p>
  </section>
</main>
</body>
</html>
```